Vanta Roving Car Wash and Detail Services, 'needs a logo and card design'

I need a logo and Card design for a new company based in Perth Western Australia called, 'Vanta Roving Car Wash and Detail Services'. I want to offer a mobile car wash and detail service across all the Perth metropolitan areas at lower prices, and offer more reliability. I would like to see designs with colours such as red, white, and black. The final design should communicate trust reliability and confidence in the services I can provide. The card must include my first name 'Ormand' and my mobile number '0417208364' for an obligation free quote.

Target Market(s)

Aimed at anyone who owns and drives a motor vehicle.

Industry/Entity Type

It Company

Contact Information for Business Card

Business Name'Vanta Roving Car Wash and Detail Services', My first name 'Ormand', and my mobile phone '0417208364' for an obligation free quote.

Font styles to use
Serif
Decorative
Script

Colors
ffffff
000000
d3d3d3
ec1f27
7f7f7f

Requirements
Must have
• Business Name'Vanta Roving Car Wash and Detail Services', My first name 'Ormand', and my mobile phone '0417208364' for an obligation free quote.
• Logo design
Nice to have
• A slogan, such as 'I come to you, and wash your car wherever you are' to let customers know I am at their service.
• Car design 'shine and clean feeling'

```html
<!DOCTYPE html>
<html lang="en">
<head>
<meta charset="utf-8">
<title>Vanta Roving Car Wash and Detail Services – Business Card</title>
<link href="https://fonts.googleapis.com/css2?family=Montserrat:wght@500;700;800&family=Orbitron:wght@700;800&display=swap" rel="stylesheet">
<style>
  :root {
    --red: #ec1f27;
    --white: #ffffff;
    --black: #000000;
    --charcoal: #2a2a2c;
    --charcoal-deep: #1c1c1e;
    --grey-light: #d3d3d3;
    --grey: #7f7f7f;
    --page: #e6e6e6;
  }
  * { margin: 0; padding: 0; box-sizing: border-box; }
  html, body {
    width: 1200px;
    height: 880px;
    overflow: hidden;
    background: var(--page);
    font-family: "Montserrat", sans-serif;
  }
  .canvas {
    width: 1200px;
    height: 880px;
    display: flex;
    flex-direction: column;
    align-items: center;
    justify-content: center;
    gap: 34px;
  }
  .card {
    position: relative;
    width: 600px;
    height: 343px;
    border-radius: 22px;
    overflow: hidden;
    box-shadow: 0 10px 28px rgba(0,0,0,0.25);
  }

  /* ---------- back face ---------- */
  .card-back {
    background: radial-gradient(ellipse at 50% 45%, var(--charcoal) 0%, var(--charcoal-deep) 100%);
    display: flex;
    align-items: center;
    justify-content: center;
  }
  .brand {
    display: flex;
    align-items: center;
    gap: 14px;
  }
  .brand-dot {
    width: 22px;
    height: 22px;
    border-radius: 50%;
    background: var(--red);
    flex: none;
  }
  .brand-name {
    font-family: "Montserrat", sans-serif;
    font-weight: 800;
    color: var(--red);
    text-transform: uppercase;
    line-height: 1.15;
  }
  .card-back .brand-name { font-size: 30px; }
  .card-back .brand-name small {
    display: block;
    font-size: 13px;
    letter-spacing: 1.5px;
    font-weight: 800;
  }

  /* ---------- front face ---------- */
  .card-front { background: var(--charcoal-deep); }
  .front-top {
    position: absolute;
    left: 0; top: 0;
    width: 100%;
    height: 168px;
    background: var(--white);
    display: flex;
    align-items: center;
    justify-content: center;
    padding-left: 90px;
  }
  .card-front .brand-name { font-size: 28px; }
  .card-front .brand-name small {
    display: block;
    font-size: 12px;
    letter-spacing: 1.4px;
    font-weight: 800;
  }
  .slogan-band {
    position: absolute;
    left: 0; top: 168px;
    width: 100%;
    height: 40px;
    background: var(--red);
    display: flex;
    align-items: center;
    padding-left: 36px;
  }
  .slogan {
    color: var(--white);
    font-size: 15px;
    font-weight: 500;
    letter-spacing: 0.2px;
  }
  .front-bottom {
    position: absolute;
    left: 0; top: 208px;
    width: 100%;
    height: 135px;
    background: radial-gradient(ellipse at 40% 30%, var(--charcoal) 0%, var(--charcoal-deep) 100%);
    display: flex;
    align-items: center;
    padding-left: 58px;
  }
  .owner-name {
    font-family: "Orbitron", sans-serif;
    font-weight: 800;
    font-size: 34px;
    color: var(--red);
    letter-spacing: 1px;
    width: 180px;
  }
  .divider {
    width: 2px;
    height: 64px;
    background: var(--red);
    margin: 0 20px 0 14px;
    opacity: 0.85;
  }
  .contact-list {
    list-style: none;
    font-size: 14px;
    line-height: 1.45;
  }
  .contact-label {
    color: var(--red);
    font-weight: 700;
  }
  .contact-value {
    color: var(--white);
    font-weight: 700;
  }
</style>
</head>
<body>
<main class="canvas">

  <section class="card card-back" aria-label="Business card back">
    <div class="brand">
      <span class="brand-dot"></span>
      <p class="brand-name">Vanta Roving<small>Car Wash and Detail Services</small></p>
    </div>
  </section>

  <section class="card card-front" aria-label="Business card front">
    <div class="front-top">
      <div class="brand">
        <span class="brand-dot"></span>
        <p class="brand-name">Vanta Roving<small>Car Wash and Detail Services</small></p>
      </div>
    </div>

    <div class="slogan-band">
      <p class="slogan">I come to you, and wash your car wherever you are</p>
    </div>

    <div class="front-bottom">
      <p class="owner-name">Ormand</p>
      <span class="divider"></span>
      <ul class="contact-list">
        <li><span class="contact-label">Mobile:</span> <span class="contact-value">0417208364</span></li>
        <li><span class="contact-label">Email:</span> <span class="contact-value">hello@vantaroving.com</span></li>
      </ul>
    </div>
  </section>

</main>
</body>
</html>
```